High quality health product needs a label

If you are a top professional designer for exclusive product labels, please read on.

High quality health products are being filled into so called Quorel glass bottles (see attachment) and I want to create labels for a range of different herbs (i.e. teasel, artemesia annua) in various dosage forms (i.e. liquid, capsules and tea). The brand of these products is called velmondra.

The label for each type of herb shall have a small variance in color, i.e. teasel can have some violet and artemesia annua a green theme. The variance in color should be unique (not just 2 circles and a triangle) and abstract (i.e. no leafs). Please have a look at 2 of our labels we have created for other products.

The logo I feel comfortable with is attached in the file plindaloft. I only want to take the leaf as logo, nothing else. The color of the logo should be adapted to our needs, but a green leaf makes sense to me. The color of the logo does not change for the variations of the label.

What do I expect in terms of design:

- minimalistic
- exclusive
- luxury
- classy
- abstract
- playful
- uniqueness

The front of the label should show:
- logo
- name of the herb, i.e. teasel
- dosage form, i.e. extract
- content, i.e. 250 ml
- the 2 logos to indicate that the product is certified organic

The back will contain some basic information that I will provide once I selected your design.

The final deliverables are 4 illustrator (compatible with version 16) ai vector files for 4 different types of herbs. Once the initial design is set, we need to create 3 color variations.

Please use a 100 mm x 210 mm layout for the 500 ml syrup bottle.

Target Market(s)

people with an interest in their health

Industry/Entity Type

health

Font styles to use
Sans Serif

Requirements
Must have
• abstract, unique, luxury, high class, minimalistic
Should not have
• overloaded, too many colors,

```html
<!DOCTYPE html>
<html lang="en">
<head>
<meta charset="utf-8">
<title>Teasel Extract – Label</title>
<link rel="stylesheet" href="https://fonts.googleapis.com/css2?family=Inter:wght@400&family=Montserrat:wght@300;500&display=swap">
<style>
  :root {
    --canvas-bg: #ffffff;
    --label-bg: #ffffff;
    --label-edge: #111111;
    --brand-green: #0b5a1e;
    --violet-deep: #6f3fe0;
    --violet-mid: #8a63ea;
    --violet-soft: #c4b0f4;
    --text-white: #ffffff;
    --text-grey: #3a3a3a;
    --badge-red: #c8202a;
    --badge-green: #7ab51d;
  }
  html, body {
    margin: 0;
    width: 1200px;
    height: 1200px;
    overflow: hidden;
    background: var(--canvas-bg);
  }
  .label {
    position: absolute;
    left: 50px;
    top: 338px;
    width: 1100px;
    height: 523px;
    box-sizing: border-box;
    border: 2px solid var(--label-edge);
    background: var(--label-bg);
  }
  .brand-name {
    position: absolute;
    left: 0;
    right: 0;
    top: 34px;
    text-align: center;
    font-family: "Montserrat", sans-serif;
    font-weight: 500;
    font-size: 26px;
    letter-spacing: 3px;
    color: var(--brand-green);
  }
  .color-wash {
    position: absolute;
    left: 352px;
    top: 150px;
    width: 400px;
    height: 270px;
    border-radius: 14px 22px 30px 8px / 30px 18px 60px 40px;
    background:
      radial-gradient(ellipse 60% 45% at 50% 48%, var(--violet-deep) 0%, rgba(111,63,224,0) 100%),
      linear-gradient(180deg, rgba(196,176,244,0.55) 0%, var(--violet-mid) 25%, var(--violet-mid) 62%, var(--violet-soft) 88%, rgba(196,176,244,0.2) 100%);
  }
  .herb-name {
    position: absolute;
    left: 0;
    right: 0;
    top: 228px;
    text-align: center;
    font-family: "Inter", sans-serif;
    font-weight: 400;
    font-size: 60px;
    line-height: 60px;
    letter-spacing: 10px;
    padding-left: 14px;
    color: var(--text-white);
  }
  .title-rule {
    position: absolute;
    left: 435px;
    top: 290px;
    width: 232px;
    height: 2px;
    background: var(--text-white);
  }
  .dosage-form {
    position: absolute;
    left: 0;
    right: 0;
    top: 296px;
    text-align: center;
    font-family: "Inter", sans-serif;
    font-weight: 400;
    font-size: 42px;
    line-height: 44px;
    letter-spacing: 3px;
    padding-left: 8px;
    color: var(--text-white);
  }
  .content-volume {
    position: absolute;
    left: 367px;
    top: 481px;
    font-family: "Montserrat", sans-serif;
    font-weight: 300;
    font-size: 22px;
    letter-spacing: 1px;
    color: var(--text-grey);
  }
  .organic-badges {
    position: absolute;
    left: 641px;
    top: 473px;
  }
</style>
</head>
<body>
  <main class="label">
    <div class="brand-name">velmondra</div>

    <div class="color-wash" role="img" aria-label="Abstract violet watercolour wash behind the product name"></div>

    <div class="herb-name">TEASEL</div>
    <div class="title-rule"></div>
    <div class="dosage-form">Extract</div>

    <div class="content-volume">250 ml</div>

    <svg class="organic-badges" width="100" height="40" viewBox="0 0 100 40" role="img" aria-label="Organic certification marks">
      <circle cx="20" cy="19" r="17" fill="#ffffff" stroke="var(--badge-red)" stroke-width="2"/>
      <rect x="54" y="5" width="42" height="27" fill="var(--badge-green)"/>
    </svg>
  </main>
</body>
</html>
```